New Stationery and envelope Design Project

I need business envelopes and stationary. I would like to have office locations on both (only Riverton address) which are Riverton (Oak Brook), Lakeport, Santa Clara, Valmora. Of course in formats I can upload and have printed. Simple and very professional I am looking for. The return address/stationary address should be:

2867 North Pellam Avenue
Annex Level
Maple Ridge, Ohio 60871

Target Market(s)

I am a consultant for larger corporations

Industry/Entity Type

Consulting

Colors

Designer to choose colors to be used in the design.

Requirements
Must have
• our address, logo, very professional and clean.
Nice to have
• the names of the cities we have offices.

```html
<!DOCTYPE html>
<html lang="en">
<head>
<meta charset="utf-8">
<title>Westmere Global Stationery</title>
<link href="https://fonts.googleapis.com/css2?family=Fira+Sans:ital,wght@0,300;0,400;0,600;1,300&family=Libre+Baskerville&display=swap" rel="stylesheet">
<style>
  :root {
    --brand-blue: #0a4fc4;
    --flap-blue: #0384d9;
    --mark-blue: #1a8fe3;
    --ink: #4a4f55;
    --ink-soft: #8a8f95;
    --paper: #ffffff;
    --edge: #c9ccd0;
    --canvas: #ffffff;
  }
  * { box-sizing: border-box; margin: 0; padding: 0; }
  html, body { width: 1200px; height: 1200px; overflow: hidden; background: var(--canvas); }
  body { position: relative; font-family: "Fira Sans", Arial, sans-serif; color: var(--ink); }

  .sheet {
    position: absolute;
    background: var(--paper);
    border: 1px solid var(--edge);
  }

  /* Letterhead */
  .letterhead { left: 8px; top: 74px; width: 648px; height: 840px; box-shadow: 4px 5px 6px rgba(0,0,0,0.25); }

  .brand { position: absolute; text-align: center; }
  .brand-dot {
    display: block; margin: 0 auto 10px;
    width: 54px; height: 54px; border-radius: 50%;
    background: var(--mark-blue);
  }
  .brand-name {
    font-size: 12.5px; font-weight: 400; letter-spacing: 0.3px;
    color: var(--brand-blue); white-space: nowrap;
  }
  .letterhead .brand { left: 76px; top: 37px; width: 130px; }

  .return-address { position: absolute; font-style: normal; font-size: 9.6px; line-height: 12px; color: var(--ink); white-space: nowrap; }
  .return-address .company { color: var(--brand-blue); font-weight: 600; }
  .letterhead .return-address { left: 475px; top: 51px; }

  .letter-body { position: absolute; left: 76px; top: 218px; width: 524px; font-size: 9.8px; line-height: 17px; font-weight: 300; }
  .salutation { margin-bottom: 28px; }
  .letter-body p.para { margin-bottom: 16px; }
  .closing { margin-top: 24px; }
  .signatory { position: absolute; left: 76px; top: 588px; font-size: 9.6px; line-height: 16px; }
  .signatory .name { font-weight: 600; }
  .signatory .title { font-style: italic; font-weight: 300; color: var(--ink-soft); }

  .office-list {
    position: absolute; left: 220px; top: 792px;
    font-size: 9.8px; font-weight: 600; color: var(--brand-blue); white-space: nowrap;
  }
  .office-list .sep { margin: 0 4px; }

  /* Envelope back */
  .envelope-back { left: 448px; top: 604px; width: 724px; height: 314px; border-top: none; }
  .envelope-flap { position: absolute; left: -1px; top: 0; width: 726px; height: 98px; }

  /* Envelope front */
  .envelope-front { left: 466px; top: 750px; width: 726px; height: 314px; }
  .envelope-front .brand { left: 70px; top: 26px; width: 130px; }
  .envelope-front .return-address { left: 270px; top: 41px; }
  .address-window {
    position: absolute; left: 75px; top: 164px; width: 305px; height: 96px;
    border: 1px solid var(--edge); border-radius: 16px;
  }
  .recipient {
    position: absolute; left: 27px; top: 28px;
    font-family: "Libre Baskerville", Georgia, serif; font-size: 8.6px; line-height: 13.6px;
    text-transform: uppercase; color: var(--ink); white-space: nowrap;
  }
</style>
</head>
<body>

<section class="sheet letterhead">
  <div class="brand">
    <span class="brand-dot"></span>
    <div class="brand-name">WESTMERE GLOBAL</div>
  </div>
  <address class="return-address">
    <div class="company">Westmere Global</div>
    <div>2867 North Pellam Avenue</div>
    <div>Annex Level</div>
    <div>Maple Ridge, Ohio 60871</div>
  </address>

  <div class="letter-body">
    <p class="salutation">Dear Mr. Ward,</p>
    <p class="para">Lorem ipsum dolor sit amet, consectetur adipiscing elit. Morbi tempus ligula lorem, sit amet vehicula lorem congue in. Phasellus ullamcorper magna felis, accumsan rhoncus augue ullamcorper a. Cum sociis natoque penatibus et magnis dis parturient montes, nascetur ridiculus mus. Pellentesque sit amet ipsum mi. Mauris volutpat vel turpis ut mattis. Vestibulum aliquam augue eu mattis fermentum. Lorem ipsum dolor sit amet, consectetur adipiscing elit. Nulla facilisi. Cras suscipit odio at est adipiscing fermentum. Ut quis sem at quam tempor sollicitudin Lorem ipsum dolor sit amet, consectetur adipiscing elit. Nulla facilisi. Cras suscipit odio at est adipiscing fermentum.<br>Uteh quis sem at quam tempor non eu quam. Praesent metus enim, varius id est id, rhoncus mollis sollicitudin non ctetur nascetur ridiculus mus adipe.</p>
    <p class="para">In vel accumsan sem, ac tincidunt quam. Donec hendrerit lacinia posuere. Nunc vulputate dui accumsan ante posuere scelerisque. Morbi dictum, mi non egestas volutpat, augue lacus vehicula elit, vel commodo libero nulla sed est. Integer non consectetur purus. Proin sit amet sem ut ipsum consequat vestibulum. Pellentesque ac interdum urna. Cras eu libero eu sapien vehicula bibendum. Aliquam urna risus, sollicitudin sit amet ante eget.</p>
    <p class="closing">Thank You,</p>
  </div>

  <div class="signatory">
    <div class="name">Daniel Ward</div>
    <div class="title">President and Chief Executive Officer</div>
  </div>

  <div class="office-list">Riverton<span class="sep">|</span>Lakeport<span class="sep">|</span>Santa Clara<span class="sep">|</span>Valmora</div>
</section>

<section class="sheet envelope-back">
  <svg class="envelope-flap" viewBox="0 0 726 98" aria-hidden="true">
    <path d="M0 0 H726 L716 10 V80 Q716 96 700 96 H26 Q10 96 10 80 V10 Z" fill="var(--flap-blue)" style="filter:drop-shadow(0 3px 2px rgba(0,0,0,0.3))"/>
  </svg>
</section>

<section class="sheet envelope-front">
  <div class="brand">
    <span class="brand-dot"></span>
    <div class="brand-name">WESTMERE GLOBAL</div>
  </div>
  <address class="return-address">
    <div class="company">Westmere Global</div>
    <div>2867 North Pellam Avenue</div>
    <div>Annex Level</div>
    <div>Maple Ridge, Ohio 60871</div>
  </address>
  <div class="address-window">
    <div class="recipient">
      <div>Daniel Ward</div>
      <div>450 Harbor St. Suite 310</div>
      <div>Fairhaven, NJ, 07704</div>
    </div>
  </div>
</section>

</body>
</html>
```